Brookvale Agribusiness Consulting needs a Website Design.

We need a website design for a new company based in UK. Brookvale offers agribusiness consulting and farm design services to farmers, smallholders and the wider agribusiness industry to assist clients in adopting more sustainable and regenerative production, processing and marketing practices.
Services are offered face-to-face and on a remote platform.
Services are offered in the UK and overseas.
We would like to see designs that reflect the natural environment, business and sustainability. Desired colours; green, blue, grey. The final design should communicate professionalism in the rural economy.
The design should be able to be customized by the client to make future changes and additions.
Target Market(s)
Farmers, smallholders, and the agricultural industry in UK and overseas.
Industry/Entity Type
Agribusiness
Number of Pages Required
4 page
Look and feel
Each slider illustrates characteristics of the customer's brand and the style your logo design should communicate.

```html
<!DOCTYPE html>
<html lang="en">
<head>
<meta charset="utf-8">
<title>Brookvale Agribusiness Consulting</title>
<link href="https://fonts.googleapis.com/css2?family=Open+Sans:wght@400;600;700&display=swap" rel="stylesheet">
<style>
:root{
  --green:#6bb33a;
  --green-dark:#4f8f27;
  --ink:#333;
  --muted:#666;
  --grey-band:#e6e6e6;
  --footer:#2b2b2b;
  --footer-bottom:#1f1f1f;
  --footer-text:#9a9a9a;
  --white:#fff;
}
*{box-sizing:border-box;margin:0;padding:0}
html,body{width:880px;height:1200px;overflow:hidden}
body{font-family:"Open Sans",Arial,sans-serif;color:var(--ink);background:var(--white)}
.site-header{height:44px;display:flex;align-items:center;justify-content:space-between;padding:0 70px 0 78px;background:var(--white)}
.brand{display:flex;align-items:center;gap:7px;font-weight:700;font-size:17px;color:var(--ink)}
.brand-mark{width:14px;height:14px;border-radius:50%;background:var(--green)}
.main-nav{display:flex;height:44px}
.main-nav a{display:flex;align-items:center;padding:0 14px;font-size:8.5px;color:var(--muted);text-decoration:none;letter-spacing:.5px;text-transform:uppercase}
.main-nav a.active{background:var(--green);color:var(--white)}
.hero{position:relative;height:380px;background:linear-gradient(180deg,#7c8794 0%,#a3adb6 40%,#c9cfd2 62%,#7f9a4c 66%,#5f8a2e 100%)}
.hero-content{position:absolute;left:560px;top:118px;width:230px}
.hero-content h1{font-size:26px;font-weight:700;letter-spacing:1px;color:#111;margin-bottom:12px}
.hero-content p{font-size:10px;line-height:1.55;color:#1c1c1c;margin-bottom:18px}
.btn{display:inline-block;background:var(--green);color:var(--white);font-size:8.5px;font-weight:600;padding:9px 22px;text-transform:uppercase;letter-spacing:.4px}
.welcome{height:190px;padding:34px 80px 0;text-align:center}
.section-title{font-size:15px;font-weight:600;letter-spacing:.6px;text-transform:uppercase}
.rule{width:60px;height:2px;background:var(--green);margin:10px auto 16px}
.welcome p{font-size:9px;line-height:1.7;color:var(--muted);text-align:left}
.services{height:352px;background:var(--grey-band);padding:22px 78px 0;text-align:center}
.services .intro{font-size:9px;line-height:1.7;color:var(--muted);margin:0 40px 10px}
.services .lead{font-size:9.5px;color:var(--muted);text-transform:uppercase;letter-spacing:.3px;margin-bottom:16px}
.cards{display:flex;justify-content:space-between}
.card{width:228px;background:var(--white);text-align:left}
.card h3{background:var(--green);color:var(--white);font-size:9px;font-weight:700;padding:8px 12px;text-transform:uppercase}
.card-body{height:146px;background:var(--green-dark);padding:14px;color:var(--white);font-size:9px;line-height:1.6}
.card-photo{height:146px}
.photo-bales{background:linear-gradient(180deg,#d8c08a,#b58e4f 60%,#8e6a36)}
.photo-produce{background:linear-gradient(135deg,#b84a2c,#d89b3b 45%,#6b8d35)}
.site-footer{height:200px;background:var(--footer);padding:30px 78px 0;display:flex;justify-content:space-between;color:var(--footer-text)}
.footer-col h4{color:var(--white);font-size:9px;font-weight:700;text-transform:uppercase;margin-bottom:12px;letter-spacing:.4px}
.footer-col{font-size:8.5px;line-height:1.9}
.col-feed{width:180px}
.feed-item{margin-bottom:8px;line-height:1.5}
.feed-item b{color:#c9c9c9;font-weight:600}
.col-links{width:120px}
.col-follow{width:120px}
.social{display:flex;align-items:center;gap:8px;margin-bottom:4px}
.social i{width:16px;height:16px;border-radius:50%;border:1px solid #777;display:block}
.footer-bottom{height:34px;background:var(--footer-bottom);color:#777;font-size:8px;text-align:center;line-height:34px}
</style>
</head>
<body>
<header class="site-header">
  <div class="brand"><span class="brand-mark"></span>Brookvale</div>
  <nav class="main-nav">
    <a class="active" href="#">Home</a><a href="#">About Us</a><a href="#">Projects</a><a href="#">What We Do</a><a href="#">Services</a><a href="#">Contact</a>
  </nav>
</header>

<section class="hero" role="img" aria-label="Photograph of a large lone oak tree in a green field under a cloudy grey sky">
  <div class="hero-content">
    <h1>BROOKVALE</h1>
    <p>Brookvale offers agribusiness consulting and farm design services to farmers, smallholders and the wider agri-business industry.</p>
    <span class="btn">Click here for more info</span>
  </div>
</section>

<section class="welcome">
  <h2 class="section-title">Welcome to Brookvale</h2>
  <div class="rule"></div>
  <p>We work alongside farmers and growers to build farms that last. Our team brings years of field experience in soil health, crop planning, livestock and land management, helping every client find practical steps toward more sustainable and regenerative production. Whether you run a smallholding or a large estate, we offer advice face to face or online, across the UK and overseas, with clear plans that fit your land and your goals.</p>
</section>

<section class="services">
  <h2 class="section-title">What We Do</h2>
  <div class="rule"></div>
  <p class="intro">Brookvale is an agribusiness consulting practice that works with a wide range of clients to shape and deliver better farming systems, choosing the methods best suited to each site and guiding them from first idea to harvest.</p>
  <p class="lead">Brookvale has now established in Devon, and undertaking three work streams:</p>
  <div class="cards">
    <article class="card">
      <h3>Consulting</h3>
      <div class="card-body">Farm planning and advice on soil, water and grazing, helping clients adopt regenerative methods and build stronger, more profitable farm businesses for the long term.</div>
    </article>
    <article class="card">
      <h3>Production</h3>
      <div class="card-photo photo-bales" role="img" aria-label="Photograph of round hay bales in a harvested field"></div>
    </article>
    <article class="card">
      <h3>Marketing</h3>
      <div class="card-photo photo-produce" role="img" aria-label="Photograph of fresh vegetables on a market stall"></div>
    </article>
  </div>
</section>

<footer class="site-footer">
  <div class="footer-col col-feed">
    <h4>Latest Posts</h4>
    <p class="feed-item">New soil health workshop dates now open for spring. <b>@brookvaleuk</b></p>
    <p class="feed-item">Visit us at the county show this weekend. <b>@brookvaleuk</b></p>
    <p class="feed-item">Read our latest guide to cover crops. <b>@brookvaleuk</b></p>
  </div>
  <div class="footer-col col-links">
    <h4>Welcome</h4>
    <p>Home</p><p>About Us</p><p>Projects</p><p>What We Do</p><p>Services</p><p>Contact</p>
  </div>
  <div class="footer-col col-links">
    <h4>Information</h4>
    <p>Privacy Policy</p><p>Terms &amp; Conditions</p><p>Sitemap</p>
  </div>
  <div class="footer-col col-follow">
    <h4>Follow Us</h4>
    <div class="social"><i></i>News</div>
    <div class="social"><i></i>Updates</div>
    <div class="social"><i></i>Network</div>
    <div class="social"><i></i>Community</div>
  </div>
</footer>
<div class="footer-bottom">© 2015 Brookvale. All rights reserved.</div>
</body>
</html>
```